Business Card Design for Small Electrical Contractor

I need to update my business card into something a little more modern. We are a small electrical contracting company. We service domestic and commercial places around Sydney. We have 2 logo designs at the moment. I have uploaded both and 2 different sizes to work with.

Industry/Entity Type

Business

Contact Information for Business Card

Leo Hartigan
8/21-23 Birch Rd, Kelsworth 2087
t - (02) 9381 4720
m - 0427 815 903
E - info@hartiganelx.com.au
W - hartiganelx.com.au
ABN: 42 907 551 316

Font styles to use
Sans Serif

Requirements
Must have
• I would also like to see the below fit on somewhere aswell
• - Licensed Electrician
• - Level 2 (Cat 1 & 4)
• - Domestic
• - Commercial
• - Repairs and Installations
• - Data
Nice to have
• Try and keep similar colours as logo
Should not have
• No lightning bolts or light globes. Smart and professional please.

```html
<!DOCTYPE html>
<html lang="en">
<head>
<meta charset="utf-8">
<title>Leo Hartigan – Business Card</title>
<link href="https://fonts.googleapis.com/css2?family=Arimo:wght@400;700&display=swap" rel="stylesheet">
<style>
  :root {
    --ink: #1e1e1e;
    --orange: #f79628;
    --paper: #ffffff;
    --brand: #1f3b40;
  }
  * { margin: 0; padding: 0; box-sizing: border-box; }
  html, body {
    width: 1200px; height: 851px; overflow: hidden;
    background: var(--paper);
    font-family: "Arimo", "Helvetica Neue", Arial, sans-serif;
  }
  .canvas { position: relative; width: 1200px; height: 851px; }

  .card { position: absolute; top: 0; width: 489px; height: 851px; overflow: hidden; background: var(--paper); }
  .card--front { left: 90px; }
  .card--back { left: 621px; }

  /* Front */
  .front-panel { position: absolute; left: 0; top: 0; width: 100%; height: 663px; background: var(--ink); }
  .front-name {
    position: absolute; left: 0; width: 100%; top: 276px;
    text-align: center; color: var(--orange); font-size: 58px; font-weight: 400; letter-spacing: -0.5px;
  }
  .front-rule { position: absolute; left: 168px; top: 346px; width: 154px; height: 3px; background: var(--orange); }
  .brand-name {
    position: absolute; left: 0; width: 100%; top: 722px;
    text-align: center; color: var(--brand); font-size: 34px; font-weight: 400;
  }
  .bottom-bar { position: absolute; left: 0; top: 819px; width: 100%; height: 32px; background: var(--ink); }

  /* Back */
  .top-bar { position: absolute; left: 0; top: 0; width: 100%; height: 13px; background: var(--ink); }
  .back-name {
    position: absolute; left: 0; width: 100%; top: 144px;
    text-align: center; color: var(--ink); font-size: 60px; font-weight: 400; letter-spacing: -0.5px;
  }
  .back-rule { position: absolute; left: 169px; top: 212px; width: 153px; height: 3px; background: var(--ink); }
  .services {
    position: absolute; left: 0; width: 100%; top: 227px;
    list-style: none; text-align: center; color: var(--ink); font-size: 16.5px; line-height: 20.5px;
  }
  .contact-panel { position: absolute; left: 0; top: 434px; width: 100%; height: 385px; background: var(--orange); }
  .contact-row { position: absolute; left: 0; width: 100%; color: var(--paper); font-size: 19px; line-height: 26px; }
  .contact-row svg { position: absolute; left: 95px; width: 32px; height: 32px; }
  .contact-row .contact-text { position: absolute; left: 165px; }
  .row-address { top: 41px; } .row-address svg { top: 10px; }
  .row-phone { top: 127px; } .row-phone svg { top: 10px; }
  .row-web { top: 226px; } .row-web svg { top: -3px; }
  .row-email { top: 313px; } .row-email svg { top: -3px; }
  .abn-bar {
    position: absolute; left: 0; top: 819px; width: 100%; height: 32px; background: var(--ink);
    color: var(--paper); text-align: center; font-size: 19px; line-height: 32px;
  }
</style>
</head>
<body>
<main class="canvas">
  <section class="card card--front">
    <div class="front-panel">
      <h1 class="front-name">Leo Hartigan</h1>
      <div class="front-rule"></div>
    </div>
    <p class="brand-name">Hartigan Electrical</p>
    <div class="bottom-bar"></div>
  </section>

  <section class="card card--back">
    <div class="top-bar"></div>
    <h2 class="back-name">Leo Hartigan</h2>
    <div class="back-rule"></div>
    <ul class="services">
      <li>Licensed Electrician</li>
      <li>Level 2 (Cat 1 &amp; 4)</li>
      <li>Domestic</li>
      <li>Commercial</li>
      <li>Repairs and Installations</li>
      <li>Data</li>
    </ul>

    <div class="contact-panel">
      <div class="contact-row row-address">
        <svg viewBox="0 0 32 32" aria-hidden="true"><path fill="#fff" d="M16 2C10 2 6 6.5 6 12c0 7 10 18 10 18s10-11 10-18c0-5.5-4-10-10-10zm0 14a4 4 0 1 1 0-8 4 4 0 0 1 0 8z"/></svg>
        <div class="contact-text">8/21-23 Birch Rd,<br>Kelsworth 2087</div>
      </div>
      <div class="contact-row row-phone">
        <svg viewBox="0 0 32 32" aria-hidden="true"><path fill="#fff" d="M3 11c0-3 6-5 13-5s13 2 13 5v2h-6v-3h-3v3H12v-3H9v3H3zm8 3h10l5 7v6H6v-6z"/><g fill="#f79628"><rect x="12" y="18" width="2" height="2"/><rect x="15" y="18" width="2" height="2"/><rect x="18" y="18" width="2" height="2"/><rect x="12" y="21" width="2" height="2"/><rect x="15" y="21" width="2" height="2"/><rect x="18" y="21" width="2" height="2"/></g></svg>
        <div class="contact-text">T (02) 9381 4720<br>M 0427 815 903</div>
      </div>
      <div class="contact-row row-web">
        <svg viewBox="0 0 32 32" aria-hidden="true"><g fill="none" stroke="#fff" stroke-width="2.4"><circle cx="16" cy="16" r="13"/><ellipse cx="16" cy="16" rx="6" ry="13"/><line x1="3" y1="16" x2="29" y2="16"/><line x1="16" y1="3" x2="16" y2="29"/><path d="M5 9h22M5 23h22"/></g></svg>
        <div class="contact-text">hartiganelx.com.au</div>
      </div>
      <div class="contact-row row-email">
        <svg viewBox="0 0 32 32" aria-hidden="true"><path fill="none" stroke="#fff" stroke-width="3.2" d="M21 16a5 5 0 1 1-5-5 5 5 0 0 1 5 5v2a3 3 0 0 0 6 0v-2a11 11 0 1 0-4.5 8.9"/></svg>
        <div class="contact-text">info@hartiganelx.com.au</div>
      </div>
    </div>
    <div class="abn-bar">ABN: 42 907 551 316</div>
  </section>
</main>
</body>
</html>
```